Corvana Wound Care Business card design

We need a business card designed around our logo which was provided. The logo of preference is the colored. Also the colors and fonts were provided.

Target Market(s)

Our Referral partners are home health agencies.

Industry/Entity Type

Healthcare

Contact Information for Business Card

Name , Phone #, Email , Title

Requirements
Nice to have
• Creativity
Should not have
• basic

```html
<!DOCTYPE html>
<html lang="en">
<head>
<meta charset="utf-8">
<title>Corvana Wound Care – Business Card</title>
<link rel="stylesheet" href="https://fonts.googleapis.com/css2?family=Libre+Baskerville:wght@700&family=Poppins:wght@400;600&display=swap">
<style>
  :root {
    --stage: #d9d9d9;
    --navy: #0a4288;
    --navy-deep: #053273;
    --sky: #1fa9e4;
    --mid-blue: #1b6cc0;
    --white: #ffffff;
  }
  * { box-sizing: border-box; margin: 0; padding: 0; }
  html, body { width: 1200px; height: 889px; overflow: hidden; }
  body {
    background: var(--stage);
    position: relative;
    font-family: "Poppins", sans-serif;
    color: var(--white);
  }
  .card {
    position: absolute;
    width: 560px;
    height: 320px;
    background: linear-gradient(120deg, var(--navy-deep) 0%, var(--navy) 60%, #0b4a8e 100%);
    overflow: hidden;
    box-shadow: 0 18px 30px rgba(0, 0, 0, 0.18);
  }
  .card--front { left: 60px; top: 90px; }
  .card--back { left: 580px; top: 480px; }

  /* soft tonal fields where the brand pattern sits */
  .decor {
    position: absolute;
    inset: 0;
    pointer-events: none;
  }
  .card--front .decor {
    background:
      radial-gradient(circle at 87% 38%, rgba(31, 169, 228, 0.85) 0, rgba(31, 169, 228, 0.55) 38px, rgba(31, 169, 228, 0) 72px),
      radial-gradient(circle at 74% 78%, rgba(31, 169, 228, 0.85) 0, rgba(31, 169, 228, 0.55) 38px, rgba(31, 169, 228, 0) 72px),
      radial-gradient(circle at 62% 16%, rgba(27, 108, 192, 0.9) 0, rgba(27, 108, 192, 0.55) 50px, rgba(27, 108, 192, 0) 90px),
      radial-gradient(circle at 93% 100%, rgba(27, 108, 192, 0.8) 0, rgba(27, 108, 192, 0.4) 40px, rgba(27, 108, 192, 0) 70px),
      radial-gradient(circle at 96% 0%, rgba(27, 108, 192, 0.7) 0, rgba(27, 108, 192, 0) 40px);
  }
  .card--back .decor {
    background:
      radial-gradient(circle at 13% 30%, rgba(31, 169, 228, 0.75) 0, rgba(31, 169, 228, 0.45) 30px, rgba(31, 169, 228, 0) 60px),
      radial-gradient(circle at 20% 96%, rgba(27, 108, 192, 0.85) 0, rgba(27, 108, 192, 0.5) 45px, rgba(27, 108, 192, 0) 85px),
      radial-gradient(circle at 78% 6%, rgba(27, 108, 192, 0.85) 0, rgba(27, 108, 192, 0.5) 50px, rgba(27, 108, 192, 0) 90px),
      radial-gradient(circle at 92% 50%, rgba(31, 169, 228, 0.8) 0, rgba(31, 169, 228, 0.5) 32px, rgba(31, 169, 228, 0) 62px);
  }

  .brand {
    position: absolute;
    display: flex;
    align-items: center;
    gap: 9px;
    font-family: "Poppins", sans-serif;
    font-weight: 600;
    color: var(--white);
    white-space: nowrap;
    line-height: 1;
  }
  .brand__square {
    background: var(--white);
    border-radius: 3px;
    flex: none;
  }
  .card--front .brand { left: 34px; top: 44px; font-size: 20px; }
  .card--front .brand__square { width: 20px; height: 20px; }
  .card--back .brand {
    left: 0; right: 0; top: 0; bottom: 0;
    justify-content: center;
    font-size: 26px;
  }
  .card--back .brand__square { width: 26px; height: 26px; }

  .person {
    position: absolute;
    left: 34px;
    top: 138px;
  }
  .person__name {
    font-family: "Libre Baskerville", serif;
    font-weight: 700;
    font-size: 22px;
    line-height: 1.1;
  }
  .person__title {
    font-size: 12px;
    margin-top: 5px;
  }
  .contact {
    position: absolute;
    left: 34px;
    bottom: 32px;
    list-style: none;
    font-size: 12px;
    line-height: 1.85;
  }
  .contact__item { display: flex; align-items: center; gap: 9px; }
  .contact__icon { width: 10px; height: 10px; flex: none; fill: var(--white); }
</style>
</head>
<body>
  <section class="card card--front" aria-label="Business card front">
    <div class="decor" role="img" aria-label="Soft blue brand pattern field"></div>
    <div class="brand"><span class="brand__square"></span>Corvana Wound Care</div>
    <div class="person">
      <h1 class="person__name">Person Name</h1>
      <p class="person__title">Designation</p>
    </div>
    <ul class="contact">
      <li class="contact__item">
        <svg class="contact__icon" viewBox="0 0 24 24"><path d="M6.6 10.8a15 15 0 0 0 6.6 6.6l2.2-2.2a1 1 0 0 1 1-.25 11.4 11.4 0 0 0 3.6.57 1 1 0 0 1 1 1V20a1 1 0 0 1-1 1A17 17 0 0 1 3 4a1 1 0 0 1 1-1h3.5a1 1 0 0 1 1 1c0 1.25.2 2.45.57 3.6a1 1 0 0 1-.25 1z"/></svg>
        123-456-789
      </li>
      <li class="contact__item">
        <svg class="contact__icon" viewBox="0 0 24 24"><path d="M2 5h20v14H2zm2 2v.4l8 5 8-5V7zm0 2.7V17h16V9.7l-8 5z"/></svg>
        hello@corvanawound.com
      </li>
      <li class="contact__item">
        <svg class="contact__icon" viewBox="0 0 24 24"><path d="M12 2a10 10 0 1 0 0 20 10 10 0 0 0 0-20zm0 2c.9 0 2.2 1.8 2.7 5H9.3C9.8 5.8 11.1 4 12 4zM4.3 11h3c0 .7 0 1.4.1 2h-3a8 8 0 0 1 0-2zm5 0h5.4a18 18 0 0 1 0 2H9.3a18 18 0 0 1 0-2zm7.4 0h3a8 8 0 0 1 0 2h-3c.1-.6.1-1.3 0-2zM9.3 15h5.4c-.5 3.2-1.8 5-2.7 5s-2.2-1.8-2.7-5z"/></svg>
        www.corvanawound.com
      </li>
    </ul>
  </section>

  <section class="card card--back" aria-label="Business card back">
    <div class="decor" role="img" aria-label="Soft blue brand pattern field"></div>
    <div class="brand"><span class="brand__square"></span>Corvana Wound Care</div>
  </section>
</body>
</html>
```